Corporate Christmas Card Email Template Design

We need a Corporate Christmas Card Design to Email all our customers with our Corporate Logos in it.

Our company deals in Machine Tools & Accessories, you will find out more about us in our web site www.valtorin.com.sg

Valtorin Tools is the distributor, so its logo should be the most prominent followed by the rest of the product logos.

Target Market(s)

Mechanical Engineers

Industry/Entity Type

It Company

Requirements
Must have
• It should not take my customers too long to open the email.

Nice to have
• It will be nice if its humorous.

It would be nice to see moving graphics.

```html
<!DOCTYPE html>
<html lang="en">
<head>
<meta charset="utf-8">
<title>Season's Greetings – Valtorin Tools</title>
<link rel="stylesheet" href="https://fonts.googleapis.com/css2?family=Great+Vibes&family=Oswald:wght@500&display=swap">
<style>
  :root {
    --page: #ffffff;
    --red-deep: #7a0d12;
    --red-mid: #a3161c;
    --red-light: #c22a2c;
    --snow: #ffffff;
    --gold: #f4d9a8;
    --brand-red: #8a1538;
    --partner-ink: #2a3f7a;
  }
  html, body {
    margin: 0;
    width: 1200px;
    height: 899px;
    overflow: hidden;
    background: var(--page);
  }
  .card {
    position: relative;
    width: 1200px;
    height: 899px;
    font-family: "Oswald", sans-serif;
  }
  .winter-scene {
    position: absolute;
    left: 0;
    top: 0;
    width: 1200px;
    height: 640px;
    background:
      radial-gradient(ellipse 48% 44% at 52% 42%, var(--red-light) 0%, var(--red-mid) 45%, var(--red-deep) 78%, rgba(122,13,18,0) 100%),
      var(--snow);
  }
  .tree-line {
    position: absolute;
    left: 0;
    top: 440px;
    width: 1200px;
    height: 200px;
    background: linear-gradient(to bottom, rgba(255,255,255,0) 0%, rgba(255,255,255,0.75) 45%, var(--snow) 100%);
  }
  .greeting {
    position: absolute;
    margin: 0;
    font-family: "Great Vibes", cursive;
    font-weight: 400;
    color: var(--gold);
    line-height: 1;
    text-shadow: 0 1px 2px rgba(60,0,0,0.4);
  }
  .greeting--season { left: 248px; top: 218px; font-size: 64px; }
  .greeting--and    { left: 536px; top: 312px; font-size: 46px; }
  .greeting--year   { left: 418px; top: 370px; font-size: 72px; }

  .partners {
    position: absolute;
    left: 88px;
    top: 676px;
    width: 700px;
    display: grid;
    grid-template-columns: repeat(5, 1fr);
    row-gap: 30px;
    column-gap: 14px;
  }
  .partner {
    font-size: 20px;
    color: var(--partner-ink);
    white-space: nowrap;
    letter-spacing: 0.5px;
  }
  .distributor {
    position: absolute;
    left: 826px;
    top: 640px;
    display: flex;
    align-items: center;
    gap: 18px;
  }
  .distributor__dot {
    width: 70px;
    height: 70px;
    border-radius: 50%;
    background: var(--brand-red);
  }
  .distributor__name {
    font-size: 48px;
    color: var(--brand-red);
    line-height: 1;
    white-space: nowrap;
  }
</style>
</head>
<body>
  <main class="card">
    <div class="winter-scene" role="img" aria-label="Red festive background framed by a snowy border with snowflakes and sparkles"></div>
    <div class="tree-line" role="img" aria-label="Row of snow-covered fir trees on a white snowy ground"></div>

    <h1 class="greeting greeting--season">Season's Greetings</h1>
    <p class="greeting greeting--and">and...</p>
    <p class="greeting greeting--year">Happy New Year!</p>

    <ul class="partners" style="list-style:none;padding:0;margin:0;">
      <li class="partner">Tarvo</li>
      <li class="partner">Rollmark</li>
      <li class="partner">Ostrel Franz</li>
      <li class="partner">Kellbar</li>
      <li class="partner">Flexano</li>
      <li class="partner">Brenmetal</li>
      <li class="partner">Vesk</li>
      <li class="partner">Halvorn</li>
      <li class="partner">Pinecut</li>
      <li class="partner">Ardentis</li>
    </ul>

    <div class="distributor">
      <span class="distributor__dot" aria-hidden="true"></span>
      <span class="distributor__name">Valtorin Tools</span>
    </div>
  </main>
</body>
</html>
```